Folder Design (inside and out) for a medical technology company

We are a Medical Technology company looking for a professional folder design.
Folder design is for Front, Back, and the flaps inside the folder. We've provided a variety of products at a national level for 20 years, we're targeting a demographic of doctors and are looking to improve out materials.

I attached our logo for reference, please feel free to reach out if you have any questions. Please use the pink and blue logo.

Thank you.

Target Market(s)

Doctors

Industry/Entity Type

Medical, Technology

Requirements
Must have
• Professional design

```html
<!DOCTYPE html>
<html lang="en">
<head>
<meta charset="utf-8">
<title>Lumora Medical – Presentation Folder</title>
<link rel="stylesheet" href="https://fonts.googleapis.com/css2?family=Varela+Round&family=Open+Sans:wght@400;600;700&family=Great+Vibes&display=swap">
<style>
  :root {
    --pink: #e9668f;
    --pink-deep: #d9567f;
    --pink-soft: #f3a9c0;
    --blue: #7a9ed4;
    --blue-deep: #6a8fc9;
    --blue-soft: #b9cde9;
    --paper: #f1f1f2;
    --paper-white: #fafafa;
    --ink: #2a2a2a;
    --label: #111;
  }
  * { box-sizing: border-box; margin: 0; padding: 0; }
  html, body { width: 1200px; height: 853px; overflow: hidden; background: #ffffff; }
  .canvas { position: relative; width: 1200px; height: 853px; font-family: "Open Sans", sans-serif; }

  .side-label {
    position: absolute; font-family: "Open Sans", sans-serif; font-weight: 700;
    font-size: 12px; letter-spacing: .3px; color: var(--label); transform: translateX(-50%);
    white-space: nowrap;
  }

  .panel { position: absolute; width: 512px; height: 310px; overflow: hidden; box-shadow: 0 2px 6px rgba(0,0,0,.12); }
  .panel svg.art { position: absolute; inset: 0; width: 100%; height: 100%; }

  .brand-name { font-family: "Varela Round", sans-serif; color: var(--blue-deep); line-height: 1; white-space: nowrap; }
  .tagline { font-family: "Varela Round", sans-serif; color: var(--pink); white-space: nowrap; }

  /* Back cover */
  .back-cover { left: 58px; top: 72px; }
  .back-cover .lockup { position: absolute; left: 262px; top: 66px; text-align: right; }
  .back-cover .brand-name { font-size: 24px; }
  .back-cover .tagline { font-size: 10px; margin-top: 5px; }
  .back-cover .contact {
    position: absolute; left: 250px; top: 113px; width: 190px;
    border-top: 1px solid #555; padding-top: 3px;
    font-size: 6.3px; line-height: 1.5; color: var(--ink); text-align: center; white-space: nowrap;
  }

  /* Front cover */
  .front-cover { left: 570px; top: 72px; }
  .front-cover .lockup { position: absolute; right: 79px; top: 18px; text-align: right; }
  .front-cover .brand-name { font-size: 29px; }
  .front-cover .tagline { font-size: 11px; margin-top: 8px; }
  .front-cover .anniversary {
    position: absolute; right: 38px; bottom: 86px; color: #fff; text-align: right;
    font-family: "Great Vibes", cursive; font-size: 14px; line-height: 1.1;
  }
  .anniversary .years-number { font-family: "Open Sans", sans-serif; font-weight: 700; font-size: 30px; vertical-align: middle; }

  /* Inside flaps */
  .inside-front { left: 58px; top: 490px; }
  .inside-back { left: 570px; top: 490px; }
  .watermark { position: absolute; top: 42px; opacity: .22; text-align: right; }
  .watermark .brand-name { font-size: 40px; color: var(--blue); }
  .watermark .tagline { font-size: 17px; margin-top: 10px; }
  .inside-front .watermark { left: 147px; }
  .inside-back .watermark { left: 200px; }

  .pocket-badge {
    position: absolute; left: 50%; top: 185px; transform: translateX(-50%);
    width: 90px; height: 44px; border-radius: 50%; background: #fff;
    display: flex; flex-direction: column; align-items: center; justify-content: center;
  }
  .pocket-badge .brand-name { font-size: 10px; }
  .pocket-badge .tagline { font-size: 4.5px; margin-top: 3px; }
</style>
</head>
<body>
<main class="canvas">

  <span class="side-label" style="left:362px; top:40px;">BACK</span>
  <span class="side-label" style="left:835px; top:40px;">FRONT</span>
  <span class="side-label" style="left:362px; top:458px;">FRONT INSIDE</span>
  <span class="side-label" style="left:835px; top:458px;">BACK INSIDE</span>

  <!-- Back cover -->
  <section class="panel back-cover">
    <svg class="art" viewBox="0 0 512 310" preserveAspectRatio="none">
      <rect width="512" height="310" fill="var(--paper)"/>
      <path d="M0,10 C110,160 330,270 512,150 L512,310 L0,310 Z" fill="#f7c6d5"/>
      <path d="M0,24 C110,175 330,285 512,170 L512,310 L0,310 Z" fill="var(--pink-soft)"/>
      <path d="M0,40 C110,195 330,300 512,195 L512,310 L0,310 Z" fill="var(--pink)"/>
      <path d="M0,150 C160,250 360,300 512,250 L512,310 L0,310 Z" fill="var(--pink-deep)" opacity=".35"/>
    </svg>
    <div class="lockup">
      <div class="brand-name">Lumora Medical</div>
      <div class="tagline">Better tools for healthier patients</div>
    </div>
    <div class="contact">
      2240 Harbor View Blvd Ste 110, Coral Bay, FL 33012<br>
      Phone : 800.555.0142 &nbsp;Mail : info@lumoramedical.example
    </div>
  </section>

  <!-- Front cover -->
  <section class="panel front-cover">
    <svg class="art" viewBox="0 0 512 310" preserveAspectRatio="none">
      <rect width="512" height="310" fill="var(--paper-white)"/>
      <path d="M0,200 C40,250 90,290 130,310 L0,310 Z" fill="#d6e1f1"/>
      <path d="M110,310 C250,260 440,190 512,0 L512,310 Z" fill="var(--blue-soft)"/>
      <path d="M140,310 C270,270 450,210 512,30 L512,310 Z" fill="var(--blue)"/>
    </svg>
    <div class="lockup">
      <div class="brand-name">Lumora Medical</div>
      <div class="tagline">Better tools for healthier patients</div>
    </div>
    <div class="anniversary">Happy to Serving<br>from <span class="years-number">20</span> Years</div>
  </section>

  <!-- Front inside flap -->
  <section class="panel inside-front">
    <svg class="art" viewBox="0 0 512 310" preserveAspectRatio="none">
      <defs>
        <linearGradient id="insideFrontSky" x1="0" y1="0" x2="0" y2="1">
          <stop offset="0" stop-color="#cfd8e6"/><stop offset="1" stop-color="#e9edf3"/>
        </linearGradient>
      </defs>
      <rect width="512" height="310" fill="url(#insideFrontSky)"/>
      <path d="M512,0 C480,60 430,120 360,150 L512,150 Z" fill="var(--blue-soft)"/>
      <path d="M512,20 C485,80 440,125 380,150 L512,150 Z" fill="var(--blue)"/>
      <path d="M0,130 C5,140 8,150 10,150 L0,150 Z" fill="var(--blue)"/>
      <path d="M0,158 L512,158 L512,270 Q512,282 500,282 L14,282 Q0,282 0,270 Z" fill="var(--blue)" role="img" aria-label="Pocket flap with a diagonal stripe pattern in light blue tones"/>
    </svg>
    <div class="watermark">
      <div class="brand-name">Lumora Medical</div>
      <div class="tagline">Better tools for healthier patients</div>
    </div>
    <div class="pocket-badge">
      <div class="brand-name">Lumora Medical</div>
      <div class="tagline">Better tools for healthier patients</div>
    </div>
  </section>

  <!-- Back inside flap -->
  <section class="panel inside-back">
    <svg class="art" viewBox="0 0 512 310" preserveAspectRatio="none">
      <rect width="512" height="310" fill="var(--paper)"/>
      <path d="M0,0 C20,70 70,120 150,150 L0,150 Z" fill="var(--pink-soft)"/>
      <path d="M0,25 C25,90 70,125 130,150 L0,150 Z" fill="var(--pink)"/>
      <path d="M512,120 C505,135 500,145 496,150 L512,150 Z" fill="var(--pink)"/>
      <path d="M0,158 L512,158 L512,270 Q512,282 500,282 L14,282 Q0,282 0,270 Z" fill="var(--pink)" role="img" aria-label="Pocket flap with a diagonal stripe pattern in pink tones"/>
    </svg>
    <div class="watermark">
      <div class="brand-name">Lumora Medical</div>
      <div class="tagline">Better tools for healthier patients</div>
    </div>
    <div class="pocket-badge">
      <div class="brand-name">Lumora Medical</div>
      <div class="tagline">Better tools for healthier patients</div>
    </div>
  </section>

</main>
</body>
</html>
```